Pinecrest

Full Color 1/8 page newspaper ad . We are 1 stop shop for all mobility needs. Highlight Accessible Van Rentals & Sales. 50 free miles on your rental when you mention this ad.

```html
<!DOCTYPE html>
<html lang="en">
<head>
<meta charset="utf-8">
<title>Pinecrest Access &amp; Mobility – Newspaper Ad</title>
<link href="https://fonts.googleapis.com/css2?family=Montserrat:wght@500;600;700;800&display=swap" rel="stylesheet">
<style>
  :root {
    --navy: #231d5c;
    --sky: #9cc3ea;
    --olive: #a9a980;
    --olive-text: #8c8c5c;
    --mauve: #9f97a3;
    --paper-top: #eceef0;
    --paper: #ffffff;
    --rule: #d9dadd;
    --ink-dark: #2e2e2e;
  }
  * { box-sizing: border-box; margin: 0; padding: 0; }
  html, body { width: 900px; height: 1200px; overflow: hidden; }
  body { font-family: "Montserrat", Arial, sans-serif; background: var(--paper); }

  .ad {
    position: relative;
    width: 900px; height: 1200px;
    background: linear-gradient(180deg, var(--paper-top) 0%, var(--paper) 45%);
    overflow: hidden;
  }

  .tagline {
    position: absolute; top: 46px; left: 0; width: 100%;
    text-align: center; color: var(--sky);
    font-weight: 700; font-size: 44px; line-height: 48px; letter-spacing: -0.5px;
  }
  .tagline-box {
    position: absolute; top: 102px; left: 147px; width: 605px; height: 60px;
    background: var(--sky); color: #fff;
    font-weight: 800; font-size: 49px; letter-spacing: -0.5px;
    display: flex; align-items: center; justify-content: center;
  }
  .headline {
    position: absolute; top: 196px; left: 0; width: 100%;
    text-align: center; color: var(--navy);
    font-weight: 800; font-size: 59px; line-height: 64px; letter-spacing: 0.5px;
  }

  .stripes { position: absolute; left: 0; top: 430px; width: 900px; height: 280px; }

  .photo-van {
    position: absolute; left: 80px; top: 384px; width: 755px; height: 304px;
    border-radius: 40px 60px 30px 30px;
    background: linear-gradient(160deg, #d3d5d9 0%, #b4b7bd 50%, #9fa3aa 100%);
  }
  .products { position: absolute; top: 700px; left: 0; width: 900px; height: 230px; }
  .product { position: absolute; border-radius: 14px; }
  .product-scooter { left: 56px; top: 8px; width: 210px; height: 214px; background: linear-gradient(160deg, #3a3436 0%, #8a2b33 70%, #5a4a4c 100%); }
  .product-walker { left: 381px; top: 18px; width: 171px; height: 208px; background: linear-gradient(160deg, #7f88ad 0%, #4d5680 60%, #3a3a44 100%); }
  .product-chair { left: 660px; top: 0; width: 171px; height: 230px; background: linear-gradient(180deg, #2a2a2e 0%, #1e1e22 55%, #34448a 100%); }
  .divider { position: absolute; top: 10px; width: 1px; height: 210px; background: var(--rule); }
  .divider-1 { left: 312px; }
  .divider-2 { left: 617px; }

  .highlight {
    position: absolute; top: 957px; left: 77px; width: 733px; height: 41px;
    border: 1.5px solid var(--olive-text);
    color: var(--olive-text); font-weight: 500; font-size: 28px; letter-spacing: 0.4px;
    display: flex; align-items: center; justify-content: center;
  }

  .mountains {
    position: absolute; top: 1016px; left: 465px; width: 435px; height: 34px;
    background: linear-gradient(180deg, #c9c4cc 0%, var(--mauve) 60%);
  }

  .band-olive-thin { position: absolute; top: 1050px; left: 0; width: 900px; height: 14px; background: var(--olive); }
  .band-navy {
    position: absolute; top: 1064px; left: 0; width: 900px; height: 92px;
    background: var(--navy); color: #fff;
  }
  .contact { position: absolute; left: 37px; top: 7px; font-weight: 500; font-size: 35px; line-height: 39px; }
  .brand {
    position: absolute; left: 510px; top: 6px; width: 340px;
    text-align: center; font-weight: 800; color: #fff;
  }
  .brand-name { font-size: 50px; line-height: 52px; letter-spacing: 0.5px; }
  .brand-sub { font-size: 25px; line-height: 28px; }

  .band-offer {
    position: absolute; top: 1156px; left: 0; width: 900px; height: 44px;
    background: var(--olive); color: var(--ink-dark);
    font-weight: 700; font-size: 23.5px; letter-spacing: 0.3px;
    display: flex; align-items: center; justify-content: center;
  }
</style>
</head>
<body>
<main class="ad">
  <p class="tagline">WE ARE 1 STOP SHOP FOR</p>
  <p class="tagline-box">ALL MOBILITY NEEDS</p>
  <h1 class="headline">ACCESSIBILITY AND<br>MOBILITY EQUIPMENT</h1>

  <svg class="stripes" viewBox="0 0 900 280" aria-hidden="true">
    <polygon points="0,264 900,10 900,42 60,258" fill="var(--sky)"/>
    <polygon points="0,266 900,46 900,66 90,262" fill="var(--navy)"/>
  </svg>

  <div class="photo-van" role="img" aria-label="Silver wheelchair-accessible minivan with side ramp deployed and a man in a power wheelchair on the ramp"></div>

  <section class="products">
    <div class="product product-scooter" role="img" aria-label="Red four-wheel mobility scooter with front basket"></div>
    <span class="divider divider-1"></span>
    <div class="product product-walker" role="img" aria-label="Blue rolling walker with seat"></div>
    <span class="divider divider-2"></span>
    <div class="product product-chair" role="img" aria-label="Black and blue power wheelchair"></div>
  </section>

  <p class="highlight">HIGHLIGHT ACCESSIBLE VAN RENTALS &amp; SALES</p>

  <div class="mountains" role="img" aria-label="Mountain range silhouette with snowy peaks"></div>

  <div class="band-olive-thin"></div>
  <footer class="band-navy">
    <p class="contact">Call us: (555) 014-2783<br>www.pinecrestaccess.com</p>
    <div class="brand">
      <p class="brand-name">PINECREST</p>
      <p class="brand-sub">ACCESS &amp; MOBILITY</p>
    </div>
  </footer>
  <p class="band-offer">50 FREE MILES ON YOUR RENTAL WHEN YOU MENTION THIS AD.</p>
</main>
</body>
</html>
```